Using Existing Logo to Create Stationary, Powerpoint and Word Background Identity

I am seeking an identity design which can be used in corporate literature and documents which extends the use of our new identity within the company logo. I need to specifically have designed background identity for a stationary set which includes a) A4 Front/Title Page (Portrait and Landscape for Proposals (Word) and Powerpoints (PPT)) b) A4 Content Pages (Same as above) c) A4 Letter Template for Letters (Word) d) Business Cards e) A5 With Compliments Slips. It is critical that the road is used in the identity sets and that content pages have clear text space in all instances.

Please read messages, as I am only seeking artwork and example placement of text in a format I can edit using photoshop. Therefore a business card would be layed out per normal with:
Name:
Company:
Mobile:
Phone:
Email:
Fax:
Address:
Web:
etc.

and stationary would have same except name removed. I have increased the budget to $260AU which has not been shown yet??
Updates

I am hoping someone can come up with a unique branding and identity using the road which can translate across business cards, proposals, presentations etc. I have seen previous work by other quality designers in this area that takes a standard logo image and creates an identity across communications documents and stationary. This is what I seek to achieve. If the identity is created for cards and proposals etc then blanks of each template can be provided as PDF, JPG and editable format (photoshop preferred) which we will alter to allow publishing to take place. Thanks

Can we fit the following on the backside of the card.

- Automating Chain of Responsibility
- Simplifying QBRTE & Velmorix
- Providing Eco-Driving & KLAP Reporting
- Protecting Transport Company Executives

Please change the back of card to these:
- Paperless QBRTE & Velmorix
- Electronic Work Diaries, Safe Driving Plans

All,

A great effort and very hard to determine who gets the gig. Each designer brings a unique flavour to this task. I have eliminated all designs that I do not consider meet the brief (per my opinion).

I will work through with those designers to elaborate the design (where needed) to finalise a design concept, which can then be closed and paid.

Please be patient, and I will be in touch shortly.

Marisol

Thanking all designers for their terrific input. We will announce shortly the design concept we are moving forward with. It has taken much deliberation and was difficult to agree upon.

Target Market(s)

Corporate Transport Customers, Government Departments

Industry/Entity Type

Business

Requirements
Must have
• Must use the existing logo imagery to consolidate into a professional identity set.
Nice to have
• Use of Road in design formats

```html
<!DOCTYPE html>
<html lang="en">
<head>
<meta charset="utf-8">
<title>Haulvane – A4 Envelopes</title>
<link rel="stylesheet" href="https://fonts.googleapis.com/css2?family=Titillium+Web:wght@400;700&display=swap">
<style>
  :root{
    --paper:#ffffff;
    --ink:#111111;
    --flap:#0d0d0d;
    --canvas:#ffffff;
    --shadow:rgba(0,0,0,.28);
    --edge:#d9d9d9;
    --road-tone-a:#1a1a1a;
    --road-tone-b:rgba(26,26,26,0);
  }
  *{margin:0;padding:0;box-sizing:border-box}
  html,body{width:1200px;height:848px;overflow:hidden;background:var(--canvas)}
  body{position:relative;font-family:"Titillium Web",Arial,sans-serif;color:var(--ink)}

  .sheet-title{position:absolute;left:86px;top:78px;font-size:11px;font-weight:700;letter-spacing:.1px}

  .envelope{position:absolute;background:var(--paper);border:1px solid var(--edge);
    box-shadow:4px 5px 8px var(--shadow);overflow:hidden}
  .envelope--back{left:81px;top:110px;width:491px;height:692px}
  .envelope--front{left:622px;top:112px;width:490px;height:690px}

  .flap{position:absolute;display:block}
  .flap--closed{left:81px;top:110px}
  .flap--open{left:622px;top:35px}

  .wordmark{position:absolute;font-weight:700;line-height:1;white-space:nowrap;text-align:right}
  .wordmark__name{display:block;color:var(--ink)}
  .wordmark__tagline{display:block;font-weight:700;color:var(--ink)}

  .envelope--back .wordmark{right:46px;bottom:42px}
  .envelope--back .wordmark__name{font-size:31px;letter-spacing:-.3px}
  .envelope--back .wordmark__tagline{font-size:8px;margin-top:2px}

  .envelope--front .wordmark{left:36px;right:auto;bottom:48px;margin-left:259px}
  .envelope--front .wordmark__name{font-size:22px;letter-spacing:-.2px}
  .envelope--front .wordmark__tagline{font-size:6px;margin-top:1px}

  .return-address{position:absolute;left:295px;bottom:16px;font-size:6.5px;line-height:1.4;font-style:normal}

  .road-area{position:absolute;left:0;bottom:0;width:240px;height:115px;
    background:linear-gradient(15deg,var(--road-tone-a) 0%,var(--road-tone-b) 55%);opacity:.45}
</style>
</head>
<body>
  <h1 class="sheet-title">A4 Envelopes</h1>

  <section class="envelope envelope--back">
    <div class="wordmark">
      <span class="wordmark__name">Haulvane</span>
      <span class="wordmark__tagline">Safer Roads Ahead</span>
    </div>
  </section>
  <svg class="flap flap--closed" width="491" height="78" viewBox="0 0 491 78" aria-hidden="true">
    <path d="M0 0 H491 L474 58 Q468 76 448 76 H43 Q23 76 17 58 Z" fill="var(--flap)"/>
  </svg>

  <svg class="flap flap--open" width="490" height="78" viewBox="0 0 490 78" aria-hidden="true">
    <path d="M0 78 L17 20 Q23 2 43 2 H447 Q467 2 473 20 L490 78 Z" fill="var(--flap)"/>
  </svg>
  <section class="envelope envelope--front">
    <div class="road-area" role="img" aria-label="Decorative road graphic sweeping in from the lower left corner"></div>
    <div class="wordmark">
      <span class="wordmark__name">Haulvane</span>
      <span class="wordmark__tagline">Safer Roads Ahead</span>
    </div>
    <address class="return-address">
      Melbourne - Head Office<br>
      Unit 4, 18 Harlow Street, Eastbrook Victoria, 3160
    </address>
  </section>
</body>
</html>
```